High end Sports Bar/ Restaurant Postcard Design

We are a high end sports bar/restaurant in forest hills on Benning street, we have high quality bar food, 24 draft beers, wine on tap and a great selection of whiskeys & scotches.
What we need is a brightly colored postcard that advertises our weekly events. It must be easy to read but eye-catching and full of fun images that will want to make people come in and drink & eat!
We are called Harlow Commons and have a gastropub feel with one entire wall covered in brick but with 9 t.v's all with audio for all sports games. We are definitely a restaurant too so its not all about sports however we will be carrying the GBX & Coastal Victory League Soccer packages.
On the back of the card we would like to advertise our lunch menu is Monday to Friday 10a.m - 3p.m. Dinner is Sunday - Monday 3p.m - 11p.m and Brunch on Saturday & Sunday. Late night bar menu also available Thursday, Friday & Saturday from 11p.m - 1a.m
Address: 54-16 Benning Street, Forest Hills, N.Y 11382 Phone number: 718 555.0143

Reason: We are extending the deadline to give us time to figure out which design is best for us, thank you all for your participation

Target Market(s)

21 - 45 year olds

Industry/Entity Type

Restaurant

Requirements
Must have
• Each individual days event must be eye-catching yet easy to read.

```html
<!DOCTYPE html>
<html lang="en">
<head>
<meta charset="utf-8">
<title>Harlow Commons – Menu Hours</title>
<link rel="stylesheet" href="https://fonts.googleapis.com/css2?family=Montserrat:wght@700;800&family=Josefin+Sans:wght@400;600&family=Lilita+One&family=Alfa+Slab+One&family=Lobster+Two:ital,wght@1,700&family=Cabin:wght@600&family=PT+Serif:ital,wght@1,700&display=swap">
<style>
  :root{
    --cream:#f6eebd;
    --butter:#f1e39a;
    --salmon:#f5ab85;
    --salmon-deep:#e98d6c;
    --brown:#4a1712;
    --navy:#1d3a63;
    --rust:#8a3a2a;
    --teal:#1f7a86;
    --crimson:#b3163e;
    --violet:#8a3bb0;
    --magenta:#c23aa8;
    --star:#f6d21b;
    --star-edge:#c8241e;
    --white:#ffffff;
    --ink:#1d1410;
  }
  *{margin:0;padding:0;box-sizing:border-box}
  html,body{width:1200px;height:930px;overflow:hidden;background:var(--cream)}
  .card{position:relative;width:1200px;height:930px;overflow:hidden;
    background:linear-gradient(120deg,var(--butter) 0%,var(--cream) 45%,#f3dcc4 100%)}
  .paint-wash{position:absolute;inset:0;
    background:radial-gradient(ellipse 420px 300px at 560px 260px,rgba(236,150,130,.35),transparent 70%),
               radial-gradient(ellipse 300px 380px at 900px 200px,rgba(236,150,130,.25),transparent 70%)}
  .beer-photo{position:absolute;left:770px;top:220px;width:430px;height:640px;
    background:linear-gradient(180deg,rgba(255,250,240,0) 0%,#fbf3e3 18%,#f3b443 40%,#e89a1f 75%,#f6ead4 100%);
    border-radius:40px 0 0 40px;opacity:.95}
  .brand-box{position:absolute;left:34px;top:40px;width:550px;height:92px;background:var(--white);
    border:6px solid var(--ink);border-radius:14px;display:flex;align-items:center;justify-content:center;
    box-shadow:2px 3px 4px rgba(0,0,0,.3)}
  .brand-name{font-family:"Montserrat",sans-serif;font-weight:800;font-size:42px;line-height:1;color:var(--brown);
    letter-spacing:1px;white-space:nowrap}
  .tel-band{position:absolute;left:584px;top:62px;width:478px;height:52px;background:var(--salmon);
    border-radius:0 12px 12px 0;border:2px solid var(--salmon-deep);display:flex;align-items:center;justify-content:center}
  .outlined{font-family:"Lilita One",sans-serif;color:var(--white);-webkit-text-stroke:2px var(--ink);paint-order:stroke fill;letter-spacing:1px;white-space:nowrap}
  .tel-band .outlined{font-size:34px}
  .price{position:absolute;left:36px;width:114px;height:114px;border-radius:50%;border:5px solid var(--white);
    box-shadow:0 2px 6px rgba(0,0,0,.3);display:flex;flex-direction:column;align-items:center;justify-content:center;
    font-family:"PT Serif",serif;font-style:italic;font-weight:700;color:var(--white);line-height:1}
  .price b{font-size:28px}.price small{font-size:18px;margin-top:6px}
  .price-lunch{top:172px;background:var(--navy)}
  .price-brunch{top:302px;background:var(--rust)}
  .hours{position:absolute;left:150px;width:495px;text-align:center}
  .hours h2{font-family:"Montserrat",sans-serif;font-weight:800;font-size:27px;line-height:1.2;letter-spacing:1px}
  .hours p{font-family:"Josefin Sans",sans-serif;font-size:29px;line-height:1.2;color:var(--ink);margin-top:4px;white-space:nowrap}
  .hours p span{font-size:25px}
  .hours .perk{font-family:"Cabin",sans-serif;font-weight:600;color:var(--rust);font-size:27px;margin-top:2px;letter-spacing:.5px}
  .lunch{top:192px}.lunch h2{color:var(--navy)}
  .brunch{top:298px}.brunch h2{color:var(--rust)}
  .dinner{top:450px}.dinner h2{color:var(--teal)}
  .late-arrow{position:absolute;left:88px;top:560px;width:560px;height:224px}
  .late-text{position:absolute;left:115px;top:612px;width:480px;text-align:center;line-height:37px}
  .late-text h3{font-family:"Montserrat",sans-serif;font-weight:800;font-size:27px;color:var(--brown);white-space:nowrap}
  .late-text .also{font-family:"Lobster Two",cursive;font-style:italic;font-weight:700;font-size:25px;color:var(--rust)}
  .late-text .days{font-family:"Alfa Slab One",serif;font-size:21px;white-space:nowrap}
  .thu{color:var(--crimson)}.fri{color:var(--violet)}.sat{color:var(--magenta)}.amp{color:var(--rust)}
  .late-text .time{font-family:"Lobster Two",cursive;font-style:italic;font-weight:700;font-size:26px;color:var(--brown)}
  .address-band{position:absolute;left:0;top:793px;width:990px;height:95px;background:var(--salmon);
    border-radius:0 14px 14px 0;border:2px solid var(--salmon-deep);box-shadow:3px 4px 6px rgba(0,0,0,.3);
    display:flex;flex-direction:column;align-items:center;justify-content:center;gap:6px}
  .address-band .outlined{font-size:27px;-webkit-text-stroke:1.6px var(--ink);display:flex;align-items:center;gap:10px}
  .web{font-family:"Montserrat",sans-serif;font-weight:700;font-size:28px;color:var(--brown);white-space:nowrap}
</style>
</head>
<body>
<main class="card">
  <div class="paint-wash" role="img" aria-label="Abstract pink and salmon paint strokes over a warm yellow background"></div>
  <div class="beer-photo" role="img" aria-label="Photo of two frosty mugs of golden draft beer with foam heads"></div>

  <header>
    <div class="brand-box"><h1 class="brand-name">HARLOW COMMONS</h1></div>
    <div class="tel-band"><span class="outlined">TEL: 718 555.0143</span></div>
  </header>

  <div class="price price-lunch"><b>$9.95</b><small>lunch</small></div>
  <div class="price price-brunch"><b>$16.95</b><small>brunch</small></div>

  <section class="hours lunch">
    <h2>LUNCH MENU</h2>
    <p>MONDAY TO FRIDAY <span>10A.M - 3P.M.</span></p>
  </section>
  <section class="hours brunch">
    <h2>BRUNCH</h2>
    <p>SATURDAY &amp; SUNDAY <span>11A.M - 3P.M</span></p>
    <p class="perk">with 2 complimentary drinks</p>
  </section>
  <section class="hours dinner">
    <h2>DINNER</h2>
    <p>SUNDAY - MONDAY <span>3P.M - 11P.M</span></p>
  </section>

  <svg class="late-arrow" viewBox="0 0 560 224" aria-hidden="true">
    <polygon points="4,6 456,6 552,112 456,218 4,218 34,112" fill="#6e3320" transform="translate(-2,4)"/>
    <polygon points="14,2 462,2 556,108 462,214 14,214 44,108" fill="#fdeee6" stroke="#6e3320" stroke-width="2"/>
    <g fill="var(--star)" stroke="var(--star-edge)" stroke-width="2">
      <polygon transform="translate(197,30)" points="0,-12 3.5,-4 12,-4 5,2 8,11 0,5.5 -8,11 -5,2 -12,-4 -3.5,-4"/>
      <polygon transform="translate(232,30)" points="0,-12 3.5,-4 12,-4 5,2 8,11 0,5.5 -8,11 -5,2 -12,-4 -3.5,-4"/>
      <polygon transform="translate(268,30)" points="0,-12 3.5,-4 12,-4 5,2 8,11 0,5.5 -8,11 -5,2 -12,-4 -3.5,-4"/>
      <polygon transform="translate(304,30)" points="0,-12 3.5,-4 12,-4 5,2 8,11 0,5.5 -8,11 -5,2 -12,-4 -3.5,-4"/>
      <polygon transform="translate(346,30)" points="0,-12 3.5,-4 12,-4 5,2 8,11 0,5.5 -8,11 -5,2 -12,-4 -3.5,-4"/>
    </g>
  </svg>
  <section class="late-text">
    <h3>LATE NIGHT BAR MENU</h3>
    <p class="also">also available</p>
    <p class="days"><span class="thu">THURSDAY</span><span class="amp">, </span><span class="fri">FRIDAY</span> <span class="amp">&amp;</span> <span class="sat">SATURDAY</span></p>
    <p class="time">from 11p.m - 1a.m</p>
  </section>

  <footer class="address-band">
    <span class="outlined">ADDRESS: 54-16 BENNING STREET, FOREST HILLS, N.Y 11382
      <svg width="22" height="22" viewBox="-12 -12 24 24" aria-hidden="true"><polygon points="0,-11 3.2,-3.6 11,-3.6 4.6,1.8 7.2,10 0,5 -7.2,10 -4.6,1.8 -11,-3.6 -3.2,-3.6" fill="#fff" stroke="#1d1410" stroke-width="1.6"/></svg>
    </span>
    <span class="web">www.harlowcommonsforesthills.com</span>
  </footer>
</main>
</body>
</html>
```